GracefulDme Business Cards

I am looking for some business cards for my business. I would like them to elegant, classy, etc.

Information Includes

Please see the the content below:

Lorinda K. Pratt

Brand titles:

Empowerment Specialist
Speaker/Workshop Facilitator

Taking you from where you are to where you're purposed to be!

Contact Information
Email - GracefulDmeOutreach@[url removed, login to view]
Facebook - [url removed, login to view]
Instagram - GracefulDme

I have attached the photos.

I am interested in possibly Orange, White, Gray concept. But open to other ideas

```html
<!DOCTYPE html>
<html lang="en">
<head>
<meta charset="utf-8">
<title>GracefulDme Business Cards</title>
<link href="https://fonts.googleapis.com/css2?family=Montserrat:wght@300;400;700&display=swap" rel="stylesheet">
<style>
  :root {
    --backdrop: #2b2d31;
    --card: #ffffff;
    --ink: #1c1c1c;
    --accent: #e2393b;
    --muted: #3d3d3d;
    --portrait-top: #d9d9dc;
    --portrait-mid: #8a8a90;
    --portrait-low: #e8474a;
  }
  * { margin: 0; padding: 0; box-sizing: border-box; }
  html, body { width: 1200px; height: 900px; overflow: hidden; }
  body {
    background: var(--backdrop);
    font-family: "Montserrat", sans-serif;
    display: flex;
    flex-direction: column;
    align-items: center;
    justify-content: center;
    gap: 34px;
  }
  .card {
    position: relative;
    width: 720px;
    height: 410px;
    background: var(--card);
    box-shadow: 0 10px 30px rgba(0,0,0,.35);
    overflow: hidden;
  }
  .portrait {
    position: absolute;
    left: 40px;
    top: 50px;
    width: 220px;
    height: 360px;
    border-radius: 90px 90px 0 0;
    background: linear-gradient(180deg, var(--portrait-top) 0%, var(--portrait-mid) 45%, var(--portrait-low) 62%, var(--portrait-low) 100%);
  }
  .identity {
    position: absolute;
    left: 300px;
    top: 110px;
  }
  .name {
    font-size: 34px;
    font-weight: 700;
    color: var(--ink);
    letter-spacing: -0.5px;
    line-height: 1.1;
  }
  .name .surname { color: var(--accent); }
  .titles {
    list-style: none;
    margin-top: 10px;
    font-weight: 300;
    font-size: 22px;
    color: var(--muted);
    line-height: 1.3;
  }
  .card--contact .identity { top: 70px; }
  .card--contact .name { font-size: 30px; }
  .card--contact .titles { font-size: 17px; margin-top: 6px; }
  .divider {
    position: absolute;
    left: 290px;
    top: 180px;
    width: 2px;
    height: 170px;
    background: var(--accent);
  }
  .contact {
    position: absolute;
    left: 320px;
    top: 230px;
  }
  .contact-icons { display: flex; gap: 16px; margin-bottom: 14px; margin-left: 40px; }
  .contact-icons span {
    width: 18px; height: 18px; border-radius: 50%;
    background: var(--ink);
  }
  .contact-icons span.is-accent { background: var(--accent); }
  .contact-lines {
    list-style: none;
    font-size: 15px;
    font-weight: 400;
    color: var(--ink);
    line-height: 1.45;
  }
</style>
</head>
<body>
  <section class="card card--front">
    <div class="portrait" role="img" aria-label="Portrait photo of Lorinda K. Pratt in a striped blouse and red skirt, arms crossed"></div>
    <div class="identity">
      <h1 class="name">Lorinda <span class="surname">K. Pratt</span></h1>
      <ul class="titles">
        <li>Evangelist</li>
        <li>Empowerment Specialist</li>
        <li>Speaker/Workshop Facilitator</li>
      </ul>
    </div>
  </section>

  <section class="card card--contact">
    <div class="portrait" role="img" aria-label="Portrait photo of Lorinda K. Pratt in a striped blouse and red skirt, arms crossed"></div>
    <div class="identity">
      <h2 class="name">Lorinda <span class="surname">K. Pratt</span></h2>
      <ul class="titles">
        <li>Evangelist</li>
        <li>Empowerment Specialist</li>
        <li>Speaker/Workshop Facilitator</li>
      </ul>
    </div>
    <div class="divider"></div>
    <div class="contact">
      <div class="contact-icons">
        <span></span>
        <span class="is-accent"></span>
        <span></span>
      </div>
      <ul class="contact-lines">
        <li>GracefulDmeOutreach@mailnest.com</li>
        <li>Friendpage.Com/GracefulDme</li>
        <li>GracefulDme</li>
      </ul>
    </div>
  </section>
</body>
</html>
```